Quilvo Garage Doors Business Card

I need a Business Card for my garage door business:
Quilvo Garage Doors.
please add:
logo
phone number: 855-3-QUILVO
(853-392)

email: service@quilvogaragedoors.com
website: www.quilvogaragedoors.com

The attached image is recommendation ONLY.

```html
<!DOCTYPE html>
<html lang="en">
<head>
<meta charset="utf-8">
<title>Quilvo Garage Doors – Business Card</title>
<link rel="stylesheet" href="https://fonts.googleapis.com/css2?family=Nunito+Sans:wght@400;600;700;800&display=swap">
<style>
  :root {
    --teal: #5fc0cc;
    --teal-dark: #3fa9b6;
    --ink: #1f1f1f;
    --white: #ffffff;
    --backdrop: #d9dadb;
    --photo-sky: #c9d3c4;
    --photo-trees: #4e6a3c;
    --photo-ground: #8b8d88;
  }
  * { box-sizing: border-box; margin: 0; padding: 0; }
  html, body { width: 1200px; height: 1200px; overflow: hidden; }
  body {
    background: var(--backdrop);
    font-family: "Nunito Sans", Arial, sans-serif;
    display: flex;
    flex-direction: column;
    align-items: center;
    justify-content: center;
    gap: 60px;
  }
  .card {
    width: 900px;
    height: 514px;
    background: var(--white);
    position: relative;
    overflow: hidden;
    box-shadow: 0 6px 18px rgba(0,0,0,0.12);
  }

  /* Front side */
  .services-band {
    height: 236px;
    background: var(--teal);
    color: var(--white);
    text-align: center;
    padding-top: 30px;
  }
  .services-list {
    font-size: 25px;
    font-weight: 400;
    line-height: 1.3;
    letter-spacing: 0.2px;
  }
  .services-list .mark { font-size: 17px; margin: 0 6px; vertical-align: 2px; }
  .emergency {
    display: flex;
    align-items: center;
    justify-content: center;
    gap: 22px;
    margin-top: 14px;
    font-size: 27px;
    font-weight: 800;
  }
  .emergency::before, .emergency::after {
    content: "";
    width: 120px;
    height: 2px;
    background: var(--white);
  }
  .team-photo {
    height: 278px;
    background: linear-gradient(180deg, var(--photo-sky) 0%, var(--photo-trees) 35%, #5d7448 65%, var(--photo-ground) 100%);
  }

  /* Back side */
  .contact-block {
    position: absolute;
    left: 70px;
    bottom: 90px;
    display: flex;
    align-items: center;
  }
  .brand {
    display: flex;
    align-items: center;
    gap: 14px;
    padding-right: 26px;
  }
  .brand-square {
    width: 48px;
    height: 48px;
    background: var(--teal);
    border-radius: 8px;
  }
  .brand-name {
    font-size: 26px;
    font-weight: 700;
    color: var(--ink);
    line-height: 1.05;
  }
  .divider {
    width: 2px;
    height: 96px;
    background: var(--teal);
    margin-right: 22px;
  }
  .contact-lines {
    list-style: none;
    font-size: 25px;
    line-height: 1.25;
    color: var(--ink);
  }
  .contact-lines .label { color: var(--teal-dark); }
</style>
</head>
<body>
  <section class="card card-front">
    <div class="services-band">
      <p class="services-list">
        <span class="mark">❖</span>Installation Garage door services <span class="mark">❖</span>Repair services<br>
        <span class="mark">❖</span>Replacement services <span class="mark">❖</span>Garage doors insulation services<br>
        <span class="mark">❖</span>Routine maintenance services
      </p>
      <p class="emergency">24 hour Emergency Response</p>
    </div>
    <div class="team-photo" role="img" aria-label="Photo of the service team in uniform standing beside the branded company pickup truck outdoors in front of trees"></div>
  </section>

  <section class="card card-back">
    <div class="contact-block">
      <div class="brand">
        <span class="brand-square"></span>
        <span class="brand-name">Quilvo<br>Garage Doors</span>
      </div>
      <span class="divider"></span>
      <ul class="contact-lines">
        <li><span class="label">Call:</span> 855-3-QUILVO(853-392)</li>
        <li><span class="label">email:</span> service@quilvogaragedoors.com</li>
        <li><span class="label">website:</span> www.quilvogaragedoors.com</li>
      </ul>
    </div>
  </section>
</body>
</html>
```